Urgent - brand new business card for a startup technical advisory and incubation business in Sydney

We need a brand new business card design for BrightForge. We are a startup technical advisory and incubation business based in Sydney Australia. We work with entrepreneurs and innovators to help rapidly and efficiently turn their ideas into reality and to ensure they have the technical platform required for growth.

Our name is partly inspired by our love of lean product development methods and the lean startup movement.

We would like clean, uncluttered designs that feature our two logo colours and communicate a professional but creative, in-touch and entrepreneurial business.

PLEASE SEE MUST HAVE PRIORITIES FOR DRAFT CONTACT INFORMATION AND OTHER DESIRED TEXT ON CARD.
Updates

We have now updated the brief to include draft business card contact information and also some additional desired text to feature on the card design.    Please review the Must Have priorities.

Also final updated source files for the horizontal and vertical versions have now been uploaded and should be used for any designs.

Thanks!

Target Market(s)

Entrepeneurs, innovators, startup investors looking for a strong product development partner

Industry/Entity Type

Business

Requirements
Must have
• Feature our two logo colours
Be a relatively clean, pared back overall design - quite minimalist

Updated source files (AI) for vertical and horizontal layouts attached.

Draft contact information for business card:
Tom Harcourt
Founder & CTO
Phone: +61 427 555123
Email: xxxx@brightforge.example
Skype: xxxxxharcourt
Twitter: tharcourt

www.brightforge.example

We would also like the overall design to include the phrase "You have great ideas. Let us make them happen." (probably in a reasonably subtle way)

Nice to have
• Inspire me! Double-sided designs are fine with logo, phrase, (URL?) on one side and contact details on other (+ any other design elements)

Logo on business card can be either with lightbulb above the wording as per example here or to the left of the BrightForge wording - both layouts in files provided.
Should not have
• Shouldn't look like a Pendrel Suite business card template :-)

```html
<!DOCTYPE html>
<html lang="en">
<head>
<meta charset="utf-8">
<title>BrightForge Business Card</title>
<link rel="stylesheet" href="https://fonts.googleapis.com/css2?family=Roboto+Condensed:wght@400;700&family=Roboto:ital,wght@0,400;1,400&display=swap">
<style>
  :root {
    --brand-blue: #12b0e8;
    --brand-ink: #1d2433;
    --text-dark: #2a2a2a;
    --canvas-bg: #ffffff;
    --card-bg: #ffffff;
    --card-shadow: rgba(0, 0, 0, 0.16);
  }
  * { margin: 0; padding: 0; box-sizing: border-box; }
  html, body {
    width: 1067px;
    height: 1200px;
    overflow: hidden;
    background: var(--canvas-bg);
  }
  .canvas {
    position: relative;
    width: 1067px;
    height: 1200px;
  }
  .card {
    position: absolute;
    left: 197px;
    width: 672px;
    height: 384px;
    background: var(--card-bg);
    box-shadow: 0 3px 10px var(--card-shadow);
  }
  .card--front { top: 164px; }
  .card--back { top: 651px; }

  /* Front */
  .brand-mark {
    position: absolute;
    left: 145px;
    top: 112px;
    width: 118px;
    height: 118px;
    border-radius: 50%;
    background: radial-gradient(circle at 45% 40%, #4cc6f0, var(--brand-blue));
  }
  .brand-name {
    position: absolute;
    left: 278px;
    top: 86px;
    font-family: "Roboto Condensed", "Arial Narrow", sans-serif;
    font-weight: 700;
    font-size: 72px;
    line-height: 1;
    letter-spacing: -1px;
    color: var(--brand-ink);
  }
  .tagline {
    position: absolute;
    left: 278px;
    top: 222px;
    font-family: "Roboto", Arial, sans-serif;
    font-style: italic;
    font-size: 17px;
    line-height: 21px;
    color: var(--text-dark);
  }

  /* Back */
  .person {
    position: absolute;
    left: 122px;
    top: 88px;
  }
  .person__name {
    font-family: "Roboto Condensed", "Arial Narrow", sans-serif;
    font-weight: 700;
    font-size: 25px;
    line-height: 30px;
    color: var(--brand-blue);
    letter-spacing: 0.2px;
  }
  .person__role {
    font-family: "Roboto", Arial, sans-serif;
    font-size: 19px;
    line-height: 24px;
    color: var(--text-dark);
  }
  .contact-list {
    position: absolute;
    left: 352px;
    top: 151px;
    list-style: none;
  }
  .contact-list__item {
    display: flex;
    align-items: center;
    height: 26.7px;
    font-family: "Roboto", Arial, sans-serif;
    font-size: 16.5px;
    color: var(--text-dark);
  }
  .contact-list__icon {
    width: 22px;
    height: 20px;
    margin-right: 18px;
    flex: none;
    fill: var(--brand-blue);
  }
</style>
</head>
<body>
<main class="canvas">

  <section class="card card--front" aria-label="Card front">
    <div class="brand-mark" aria-hidden="true"></div>
    <div class="brand-name">BrightForge</div>
    <p class="tagline">You have great ideas.<br>Let us make them happen.</p>
  </section>

  <section class="card card--back" aria-label="Card back">
    <div class="person">
      <h1 class="person__name">TOM HARCOURT</h1>
      <p class="person__role">Founder &amp; CTO</p>
    </div>
    <ul class="contact-list">
      <li class="contact-list__item">
        <svg class="contact-list__icon" viewBox="0 0 24 24" aria-hidden="true"><path d="M6.6 10.8a15 15 0 0 0 6.6 6.6l2.2-2.2a1 1 0 0 1 1-.25 11.4 11.4 0 0 0 3.6.6 1 1 0 0 1 1 1V20a1 1 0 0 1-1 1A17 17 0 0 1 3 4a1 1 0 0 1 1-1h3.5a1 1 0 0 1 1 1c0 1.25.2 2.45.6 3.6a1 1 0 0 1-.25 1z"/></svg>
        +61 427 555123
      </li>
      <li class="contact-list__item">
        <svg class="contact-list__icon" viewBox="0 0 24 24" aria-hidden="true"><path d="M2 5h20v14H2z M3.5 6.5 12 12.5l8.5-6" fill="var(--brand-blue)"/><path d="M3 6.2 12 12.4 21 6.2" fill="none" stroke="#fff" stroke-width="1.6"/></svg>
        xxxx@brightforge.example
      </li>
      <li class="contact-list__item">
        <svg class="contact-list__icon" viewBox="0 0 24 24" aria-hidden="true"><circle cx="12" cy="12" r="9.5" fill="none" stroke="var(--brand-blue)" stroke-width="2"/><ellipse cx="12" cy="12" rx="4" ry="9.5" fill="none" stroke="var(--brand-blue)" stroke-width="1.8"/><path d="M2.5 12h19" stroke="var(--brand-blue)" stroke-width="1.8"/></svg>
        www.brightforge.example
      </li>
      <li class="contact-list__item">
        <svg class="contact-list__icon" viewBox="0 0 24 24" aria-hidden="true"><circle cx="12" cy="12" r="9"/></svg>
        xxxxxharcourt
      </li>
      <li class="contact-list__item">
        <svg class="contact-list__icon" viewBox="0 0 24 24" aria-hidden="true"><circle cx="12" cy="12" r="9"/></svg>
        @tharcourt
      </li>
    </ul>
  </section>

</main>
</body>
</html>
```